TEAL BEACON LICE REMOVAL labels

I need a label design for our MINT REPELLING SHAMPOO (LICE PREVENTION).
It also includes our MINT REPELLING CONDITIONER (LICE PREVENTION) and our MINT SPRAY (LICE PREVENTION) also includes LICE & NIT ELIMINATING MOUSSE (LICE TREATMENT) and a LICE ELIMINATOR 100% Dimethicone oil (LICE TREATMENT). The shampoo and conditioner are sulfate free, contains peppermint and other essential oils and is safe for the entire family. Label should be simple, modern and high end looking. Fun is good too if it looks nice!

Target Market(s)

Kids and Adults

Industry/Entity Type

Hair Care Product

Font styles to use
Sans Serif
Decorative

Requirements
Must have
• -Words that should be used: safe, non toxic, sulfate free, essential oils, pesticide free. - Naturally removes lice, super lice & nits are great words for the lice & nit eliminating mousse and treatment oil 100% Dimethicone oil
- On a side note there are no essential oils in the lice & nit eliminating mousse or treatment oil 100% Dimethicone oil
Nice to have
• Earth tone colors if possible
Kid safe, no fillers, colors or scents
100% effective (even against super lice)
8oz labels and 4oz labels
Should not have
• No pictures of lice

```html
<!DOCTYPE html>
<html lang="en">
<head>
<meta charset="utf-8">
<title>Teal Beacon Lice Removal – Lice &amp; Nit Eliminating Mousse Label</title>
<link rel="stylesheet" href="https://fonts.googleapis.com/css2?family=Poppins:wght@300;400&family=Oswald:wght@500;600&family=Patrick+Hand&display=swap">
<style>
  :root {
    --label-bg: #f1f2f3;
    --label-bg-edge: #e2e4e6;
    --ink: #2b2b2b;
    --ink-soft: #3d3d3d;
    --blue: #3a97cf;
    --blue-rule: #2f8bc9;
    --band-light: #c3dff0;
    --band-mid: #9cc6e0;
    --brand: #cf4a1f;
    --ring: #8a8a8a;
    --dots: #9a9a9a;
    --white: #ffffff;
  }
  * { margin: 0; padding: 0; box-sizing: border-box; }
  html, body { width: 900px; height: 1200px; overflow: hidden; }
  body {
    background: linear-gradient(90deg, var(--label-bg-edge) 0%, var(--label-bg) 30%, var(--white) 50%, var(--label-bg) 70%, var(--label-bg-edge) 100%);
    font-family: "Poppins", sans-serif;
    color: var(--ink);
    position: relative;
  }
  .category {
    position: absolute; top: 66px; left: 0; width: 900px;
    display: flex; align-items: center; gap: 24px;
  }
  .category__rule { flex: 1; height: 8px; background: var(--blue-rule); }
  .category__text { font-size: 34px; font-weight: 400; color: var(--ink-soft); letter-spacing: 0.5px; }

  .brand {
    position: absolute; top: 140px; left: 320px; width: 260px; height: 260px;
  }
  .brand__ring { position: absolute; inset: 0; }
  .brand__name {
    position: absolute; inset: 0;
    display: flex; align-items: center; justify-content: center; text-align: center;
    font-family: "Poppins", sans-serif; font-weight: 400;
    font-size: 24px; line-height: 1.3; letter-spacing: 3px;
    color: var(--brand);
  }

  .product {
    position: absolute; top: 440px; left: 0; width: 900px; text-align: center;
  }
  .product__kind {
    font-weight: 300; font-size: 62px; line-height: 1.15; color: var(--blue);
  }
  .product__name {
    font-family: "Oswald", sans-serif; font-weight: 600;
    font-size: 150px; line-height: 1; margin-top: 24px; color: var(--ink);
    letter-spacing: -1px;
  }
  .product__claim {
    font-weight: 300; font-size: 46px; margin-top: 20px; color: var(--blue);
  }
  .product__note {
    font-weight: 300; font-size: 34px; color: var(--ink-soft); margin-top: -4px;
  }
  .kid-safe {
    display: inline-block; margin-top: 22px;
    background: #1f1f1f; color: var(--white);
    font-family: "Patrick Hand", cursive; font-size: 38px; line-height: 1;
    padding: 12px 30px 10px; border-radius: 40px;
  }

  .dotted-rule {
    position: absolute; top: 1014px; left: 0; width: 900px;
    border-top: 5px dotted var(--dots);
  }
  .benefits {
    position: absolute; top: 1028px; left: 0; width: 900px; text-align: center;
    font-family: "Oswald", sans-serif; font-weight: 500; font-size: 33px;
    letter-spacing: 1px; color: var(--blue);
  }
  .net-band {
    position: absolute; top: 1086px; left: 0; width: 900px; height: 114px;
    background: linear-gradient(90deg, var(--band-mid) 0%, var(--band-light) 50%, var(--band-mid) 100%);
    display: flex; align-items: center; justify-content: center;
    font-size: 34px; font-weight: 400; color: var(--ink-soft);
  }
</style>
</head>
<body>
  <header class="category">
    <span class="category__rule"></span>
    <span class="category__text">LICE TREATMENT</span>
    <span class="category__rule"></span>
  </header>

  <div class="brand">
    <svg class="brand__ring" viewBox="0 0 260 260" aria-hidden="true">
      <circle cx="130" cy="130" r="126" fill="none" stroke="var(--ring)" stroke-width="2"/>
    </svg>
    <div class="brand__name">TEAL<br>BEACON<br>LICE<br>REMOVAL</div>
  </div>

  <main class="product">
    <p class="product__kind">· LICE &amp; NIT ·<br>ELIMINATING</p>
    <h1 class="product__name">MOUSSE</h1>
    <p class="product__claim">PROVEN EFFECTIVE</p>
    <p class="product__note">(dissolves nit glue)</p>
    <span class="kid-safe">Kid safe!</span>
  </main>

  <div class="dotted-rule"></div>
  <p class="benefits">NON TOXIC • SULFATE FREE • NO CHEMICALS • PESTICIDE FREE</p>
  <footer class="net-band">NET.WT. 8 OZ</footer>
</body>
</html>
```